Information Technology Cloud Services Website

"Offer in every submission a high resolution version of your concept please. It is difficult to see of my text (sales copy) was added to your screenshot or not. It is necessary for me to provide high quality feedback."

My company provides a customizable ecosystem for Brindlewave Deskset 880 and Corvel users that includes all the technologies for organizing business processes and communications, letting my clients manage business without fear.

You can see our current site at http://www.DesksetShiftCrew.com

I currently use WordPress using the theme platform OptimizePress. If you have OptimizePress, that would be perfect, yet not required. However, I do need the finish product in WordPress for future additions and edits.

The Brand colors are Light Blue just like the logo attached.

I am in the need of graphic images on every webpage that can convey the services that my company does.

We need a refresh of our existing website that looks more 2018. We have made a mockup of the content that we want and a sample of where we want it. Nothing is set in stone, if you have better ideas of where things should go, feel free.

Here are some competitors similar sites we like - but still looking for a unique design that fits out brand

https://www.quorvatek.com/

https://www.tarnwell.com/email-migrations/deskset-880-shift-crew

https://www.gorvanta.com/solutions/mailbox-migration/

https://www.plumeridge.com/

https://www.plumeridge.com/deskset-880/

Target Market(s)

Business = IT Managers, IT Directors, IT Staff, IT Vice Presidents, Chief Information Officer

Industry/Entity Type

Information Technology

Coding

Coded - Design and coding required

Number of Pages Required

5+ page

Font styles to use
Sans Serif

Colors

Designer to choose colors to be used in the design.

Requirements
Must have
• Must have creative graphic images that convey the story/services that I offer. Its important to us that the design is very explanatory, the customer should easily be able to figure out that we provide Deskset 880 migrations services right away. Also we are looking for a new very responsive HTML5+ webpages in WordPress.

```html
<!DOCTYPE html>
<html lang="en">
<head>
<meta charset="utf-8">
<title>DesksetShiftCrew – Deskset 880 Migration Experts</title>
<link href="https://fonts.googleapis.com/css2?family=Poppins:wght@300;400;500;600;700&display=swap" rel="stylesheet">
<style>
:root{
  --sky:#1e8ff0;
  --sky-light:#3aa6f7;
  --sky-pale:#7fc4fb;
  --navy:#0d2f55;
  --navy-deep:#0a2340;
  --navy-band:#133d6b;
  --ink:#1d2b3a;
  --muted:#5d6b7a;
  --paper:#ffffff;
  --mist:#f2f4f7;
  --line:#d9dee5;
  --footer:#1c1f24;
}
*{box-sizing:border-box;margin:0;padding:0}
html,body{width:1200px;height:4511px;overflow:hidden}
body{font-family:"Poppins",Arial,sans-serif;color:var(--ink);background:var(--paper);position:relative}
.abs{position:absolute}
a{color:inherit;text-decoration:none}

/* Hero */
.hero{left:0;top:0;width:1200px;height:591px;background:linear-gradient(180deg,var(--sky-light),var(--sky))}
.brand{left:36px;top:30px;width:330px;height:50px;background:var(--navy-deep);display:flex;align-items:center;gap:10px;padding-left:18px;color:#fff;font-size:15px;font-weight:600}
.brand-dot{width:26px;height:26px;border-radius:50%;border:2px solid #fff}
.phone{right:36px;top:8px;color:#fff;font-size:14px;display:flex;gap:8px;align-items:center}
.nav{left:405px;top:32px;width:740px;height:52px;background:#fff;display:flex;align-items:center;justify-content:space-around;font-size:14px;color:var(--ink)}
.nav .active{font-weight:600;border-bottom:2px solid var(--sky);padding-bottom:4px}
.hero-art{left:90px;top:120px;width:420px;height:450px;border-radius:6px;background:linear-gradient(160deg,rgba(255,255,255,.25),rgba(13,47,85,.35))}
.hero-copy{left:612px;top:190px;width:520px;color:#fff}
.hero-copy h1{font-size:21px;font-weight:700;line-height:1.45;text-transform:uppercase}
.hero-copy p{font-size:13px;margin-top:14px;line-height:1.6}
.btn{display:inline-block;border-radius:20px;font-size:12px;padding:9px 20px;font-weight:500}
.btn-navy{background:var(--navy);color:#fff}
.hero-btns{margin-top:22px;display:flex;gap:14px}
.hero-arrows{left:548px;top:548px;color:#fff;font-size:24px;letter-spacing:18px}

/* Press */
.press{left:0;top:591px;width:1200px;height:114px;background:var(--navy-band);display:flex;align-items:center;color:#fff}
.press-label{margin-left:170px;font-size:17px}
.press-names{display:flex;gap:70px;margin-left:60px;font-size:24px;font-weight:700}

/* Intro */
.intro-img{left:171px;top:780px;width:414px;height:435px;background:linear-gradient(135deg,#9fb6cc,#3d5f82)}
.intro-text{left:615px;top:780px;width:510px;font-size:12.5px;line-height:1.85;color:var(--muted)}
.intro-text h2{font-size:17px;color:var(--navy);font-weight:600;margin:14px 0 8px}
.intro-text strong{color:var(--sky);font-weight:600}
.intro-text p+p{margin-top:10px}

/* Process */
.process{left:0;top:1290px;width:1200px;height:632px;background:var(--mist)}
.section-title{left:0;width:1200px;text-align:center;font-size:38px;font-weight:600;color:var(--navy)}
.section-title span{color:var(--sky)}
.process-sub{left:0;width:1200px;text-align:center;font-size:15px;color:var(--navy);letter-spacing:.5px}
.step-note{left:172px;top:1676px;width:166px;height:186px;background:var(--navy);color:#fff;font-size:10px;line-height:1.55;padding:16px 12px;text-align:center}

/* CTA */
.cta{left:0;top:1922px;width:1200px;height:296px;background:linear-gradient(90deg,var(--sky-light),var(--sky-pale))}
.cta-copy{left:170px;top:1975px;width:520px;color:#fff;font-size:20px;line-height:1.5}
.cta-btn{left:170px;top:2135px}
.cta-art{left:722px;top:1940px;width:462px;height:268px;border-radius:6px;background:linear-gradient(160deg,rgba(255,255,255,.45),rgba(13,47,85,.25))}

/* Migrate */
.migrate-img{left:0;top:2390px;width:590px;height:376px;border-radius:0 188px 188px 0;background:linear-gradient(120deg,#7d93ab,#2e4d70)}
.migrate-title{left:585px;top:2378px;font-size:33px;font-weight:600;color:var(--navy)}
.migrate-title span{color:var(--sky)}
.migrate-grid{left:585px;top:2460px;width:520px;display:grid;grid-template-columns:1fr 1fr;gap:36px 40px}
.service h3{font-size:14px;color:var(--navy);font-weight:600;margin-top:8px}
.service p{font-size:11px;color:var(--muted);line-height:1.5;margin-top:4px}

/* Testimonials */
.stories{left:0;top:2908px;width:1200px;height:610px;background:linear-gradient(180deg,var(--navy-band),var(--navy))}
.stories-title{left:0;top:2985px;width:1200px;text-align:center;color:#fff;font-size:25px;font-weight:500}
.stories-sub{left:0;top:3030px;width:1200px;text-align:center;color:#c9d8ea;font-size:13px;line-height:1.6}
.quote{top:3155px;width:250px;height:230px;border:1px solid rgba(255,255,255,.35);padding:40px 16px 14px;color:#e1ebf6;font-size:10.5px;line-height:1.55}
.avatar{left:105px;top:-22px;width:40px;height:40px;background:#6d87a6}
.quote .who{margin-top:16px;font-size:11.5px;color:#fff}
.quote .org{font-size:9px;text-align:center;margin-top:4px;color:#b9c9dc}
.stories-arrows{left:548px;top:3445px;color:#fff;font-size:24px;letter-spacing:18px}

/* Form */
.form-card{left:174px;top:3592px;width:420px;height:560px;background:#fff;box-shadow:0 4px 18px rgba(0,0,0,.12)}
.form-head{height:100px;background:var(--navy);color:#fff;text-align:center;padding-top:22px}
.form-head h3{font-size:17px;font-weight:600}
.form-head p{font-size:12px;color:#c9d8ea;margin-top:4px;line-height:1.4}
.field{margin:0 24px;height:64px;border-bottom:1px solid var(--line);font-size:12px;color:var(--muted);display:flex;align-items:flex-end;padding-bottom:10px}
.form-btn{display:block;margin:28px auto 0;width:210px;text-align:center}
.laptop-area{left:648px;top:3740px;width:530px;height:430px;border-radius:50%;background:linear-gradient(150deg,#1b4f86,var(--navy-deep))}

/* Footer */
.footer{left:0;top:4188px;width:1200px;height:323px;background:var(--footer);color:#d7dbe0}
.footer h4{font-size:14px;font-weight:500;color:#fff}
.footer ul{list-style:none;font-size:11px;line-height:1.9;margin-top:14px}
.foot-input{width:260px;height:26px;border-bottom:1px solid #4a4f57;font-size:9px;padding-top:10px;color:#9aa2ad}
.send{background:var(--sky);color:#fff;font-size:10px;width:80px;text-align:center;padding:5px 0;margin-top:12px}
.copyright{left:0;top:4452px;width:1200px;text-align:center;font-size:10px;color:#aab1ba;line-height:1.5}
</style>
</head>
<body>

<section class="hero abs"></section>
<div class="brand abs"><span class="brand-dot"></span>DesksetShiftCrew.com</div>
<div class="phone abs">
  <svg width="14" height="14" viewBox="0 0 24 24" fill="#fff"><path d="M6.6 10.8a15 15 0 0 0 6.6 6.6l2.2-2.2a1 1 0 0 1 1-.25 11.4 11.4 0 0 0 3.6.57 1 1 0 0 1 1 1V20a1 1 0 0 1-1 1A17 17 0 0 1 3 4a1 1 0 0 1 1-1h3.5a1 1 0 0 1 1 1c0 1.25.2 2.45.57 3.6a1 1 0 0 1-.25 1z"/></svg>
  Call us: (877) 555-0142
</div>
<nav class="nav abs">
  <a class="active">Home</a><a>Email Migrations</a><a>Migration Solutions</a><a>Mergers</a><a>Technology Services</a><a>About Us</a>
</nav>
<div class="hero-art abs" role="img" aria-label="Illustration of a man working at a desk with floating application windows"></div>
<div class="hero-copy abs">
  <h1>Are you willing to cut costs &amp; boost productivity by migrating your email server &amp;infrastructure to the cloud?</h1>
  <p>We Help Companies Quickly and Professionally<br>Migrate to Deskset 880 &amp; Corvel</p>
  <div class="hero-btns"><span class="btn btn-navy">Request a Quote</span><span class="btn btn-navy">Learn More</span></div>
</div>
<div class="hero-arrows abs">&larr;&rarr;</div>

<section class="press abs">
  <span class="press-label">As Seen In:</span>
  <div class="press-names"><span>Halvex</span><span>Orrin</span><span>Pellam News</span><span>Tavrel</span></div>
</section>

<div class="intro-img abs" role="img" aria-label="Photo collage of IT professionals working at computers"></div>
<div class="intro-text abs">
  <p>When it comes to migrating your email server, apps or infrastructure to the cloud, you don't have to lose sleep or spend over your budget. All you have to do is choose DesksetShiftCrew and we will professionally and efficiently handle every single detail.</p>
  <h2>Here's How DesksetShiftCrew Can Help Your Business</h2>
  <p><strong>SAVE TIME</strong> - Our team of experts will determine your needs and develop a 100% custom migration strategy tailored to your company. We will analyze your current environment and prepare your Deskset 880 profiles and users. You do not have to trouble yourself with all the technical details anymore.</p>
  <p><strong>SAVE EFFORT</strong> - After identifying your needs, we will start migrating your data. Your email service will be re-routed to Deskset 880 and we will help you set up the new email service on all your local desktops and mobile devices. Once the migration process is complete, we will review the results and ensure that everything went according to plan.</p>
  <p><strong>SAVE MONEY</strong> - Migrating your data to Deskset 880 means cutting down all expenses and boosting your performance. Plus, we offer you flexible monthly licenses, so you are not stuck with upfront annual contract license costs.</p>
</div>

<section class="process abs"></section>
<h2 class="section-title abs" style="top:1340px">OUR <span>MIGRATION</span> PROCESS</h2>
<p class="process-sub abs" style="top:1398px">AT ANY TIME OF THE DAY OR NIGHT, 24/7 &amp; 365 DAYS OUT OF THE YEAR</p>
<svg class="abs" style="left:0;top:1450px" width="1200" height="240" viewBox="0 0 1200 240" aria-label="Five-step migration process">
  <g fill="none" stroke="#0d2f55" stroke-width="3">
    <path d="M255 90 Q339 20 423 90"/><path d="M423 90 Q511 20 600 90"/><path d="M600 90 Q685 20 771 90"/><path d="M771 90 Q861 20 951 90"/>
  </g>
  <g fill="#0d2f55"><path d="M418 84l8 8-11 2z"/><path d="M595 84l8 8-11 2z"/><path d="M766 84l8 8-11 2z"/><path d="M946 84l8 8-11 2z"/></g>
  <g>
    <circle cx="255" cy="155" r="68" fill="#0d2f55"/><circle cx="255" cy="155" r="50" fill="#fff"/>
    <circle cx="423" cy="155" r="68" fill="#1e8ff0"/><circle cx="423" cy="155" r="50" fill="#fff"/>
    <circle cx="600" cy="155" r="68" fill="#0d2f55"/><circle cx="600" cy="155" r="50" fill="#fff"/>
    <circle cx="771" cy="155" r="68" fill="#1e8ff0"/><circle cx="771" cy="155" r="50" fill="#fff"/>
    <circle cx="951" cy="155" r="68" fill="#0d2f55"/><circle cx="951" cy="155" r="50" fill="#fff"/>
  </g>
  <g font-family="Poppins, sans-serif" font-size="12" fill="#0d2f55" text-anchor="middle">
    <text x="255" y="128">First</text><text x="255" y="143">Contact</text>
    <text x="423" y="128">Pre</text><text x="423" y="143">Migration</text>
    <text x="600" y="128">Start</text><text x="600" y="143">Migration</text>
    <text x="771" y="128">Local</text><text x="771" y="143">Setup</text>
    <text x="951" y="128">Post</text><text x="951" y="143">Migration</text>
  </g>
  <g fill="none" stroke="#1e8ff0" stroke-width="2.5">
    <rect x="244" y="160" width="22" height="16" rx="2"/>
    <path d="M412 176h22M416 170l7-8 7 8"/>
    <rect x="589" y="158" width="22" height="20" rx="2"/><path d="M589 168h22"/>
    <rect x="760" y="158" width="22" height="15" rx="2"/><path d="M765 178h12"/>
    <path d="M940 168l7 7 12-14"/>
  </g>
</svg>
<div class="step-note abs">Our team of experts will contact you to determine your needs and develop a custom migration strategy. A dedicated migration agent will be assigned to your account as the main contact for the whole migration process.</div>

<section class="cta abs"></section>
<p class="cta-copy abs">Cloud Services Like Brindlewave Deskset 880 And Corvel Can Help You Boost Your Productivity?<br>Speak With One Of Our Expert Engineers About Your Business Goals</p>
<span class="cta-btn btn btn-navy abs">Request a Quote Today!</span>
<div class="cta-art abs" role="img" aria-label="Illustration of a desk with laptop, code windows and coffee cup"></div>

<div class="migrate-img abs" role="img" aria-label="Photo of a business team meeting around a laptop"></div>
<h2 class="migrate-title abs">WHAT WE <span>MIGRATE</span></h2>
<div class="migrate-grid abs">
  <div class="service">
    <svg width="30" height="30" viewBox="0 0 30 30" fill="none" stroke="#0d2f55" stroke-width="2"><rect x="4" y="3" width="22" height="24" rx="2"/><path d="M10 15l4 4 7-8"/></svg>
    <h3>Account Directory Synchronization</h3><p>No Need To Recreate Your Account Directory</p>
  </div>
  <div class="service">
    <svg width="30" height="30" viewBox="0 0 30 30" fill="none" stroke="#0d2f55" stroke-width="2"><rect x="3" y="7" width="24" height="17" rx="2"/><path d="M3 9l12 8 12-8"/></svg>
    <h3>Mailboxes</h3><p>All Email And Data From Virtually All Email Platforms</p>
  </div>
  <div class="service">
    <svg width="30" height="30" viewBox="0 0 30 30" fill="none" stroke="#0d2f55" stroke-width="2"><path d="M8 22a6 6 0 0 1 0-12 8 8 0 0 1 15 2 5 5 0 0 1 0 10z"/></svg>
    <h3>Data Storage</h3><p>Data Storage to Deskset Cloud Storage</p>
  </div>
  <div class="service">
    <svg width="30" height="30" viewBox="0 0 30 30" fill="none" stroke="#0d2f55" stroke-width="2"><rect x="4" y="4" width="22" height="22" rx="2"/><path d="M4 12h22M12 12v14"/></svg>
    <h3>Sharefold</h3><p>From Sharefold To Sharefold Online</p>
  </div>
</div>

<section class="stories abs"></section>
<h2 class="stories-title abs">JOIN 1000'S OF PEOPLE BENEFITING FROM DESKSET 880</h2>
<p class="stories-sub abs">Lorem ipsum dolor sit amet, consectetur adipiscing elit. Aenean accumsan dolor dolor,<br>in pulvinar porttitor velit in pharetra.</p>
<div class="quote abs" style="left:172px"><span class="avatar abs"></span>
  Deskset 880 is much more than just email. It's a cloud offering that provides a whole range of communication and collaboration services that will help us stay current and optimized for success. Our subscription grew with us.
  <p class="who">Rowan Hale, Chief Technology Officer</p><p class="org">Kestrel Rail</p>
</div>
<div class="quote abs" style="left:466px"><span class="avatar abs"></span>
  With Deskset 880, maintenance employees anywhere on the network can access the emails that they need to help operate the railroad. Field teams stay in touch without chasing their manuals online.
  <p class="who">Mara Quint, Chief Information Officer</p><p class="org">Kestrel Rail</p>
</div>
<div class="quote abs" style="left:758px"><span class="avatar abs"></span>
  Deskset 880 is much more than just email. It's a cloud offering that provides a whole range of communication and collaboration services that will help us stay current and optimized for success. Our subscription grew with us.
  <p class="who">Rowan Hale, Chief Technology Officer</p><p class="org">Kestrel Rail</p>
</div>
<div class="stories-arrows abs">&larr;&rarr;</div>

<form class="form-card abs">
  <div class="form-head"><h3>Ready To Start Migrating?</h3><p>Speak With One Of Our Expert Engineers About<br>Your Business Goals</p></div>
  <div class="field">First Name</div><div class="field">Last Name</div><div class="field">Company Name</div>
  <div class="field">Email</div><div class="field">Phone</div><div class="field">Title</div>
  <span class="form-btn btn btn-navy">Talk with an Expert Today!</span>
</form>
<div class="laptop-area abs" role="img" aria-label="Laptop showing a video call, set on a dark blue circle"></div>

<footer class="footer abs">
  <div class="abs" style="left:174px;top:36px">
    <h4>Shown Expanded</h4>
    <ul><li>Quillbox Mail Migration</li><li>Mailhub Migration</li><li>Ganterra Suite Migration</li><li>Hybrid Configurations</li><li>Ostrava Notes Migration</li><li>Mail Archive Migration</li><li>Legacy Archive Migration</li></ul>
  </div>
  <div class="abs" style="left:392px;top:36px">
    <h4>Connect Us</h4>
    <ul><li>Harlow Consulting, LLC</li><li>418 Alder Row, Suite 210</li><li>Linford, WY 82990</li><li>Toll-Free: (877) 555-0142</li><li>Email:</li><li>Inquiries@DesksetShiftCrew.com</li></ul>
  </div>
  <div class="abs" style="left:685px;top:36px">
    <h4>CONTACT FROM</h4>
    <div class="foot-input">NAME</div><div class="foot-input">EMAIL</div><div class="foot-input">PHONE</div><div class="foot-input">MESSAGE</div>
    <div class="send">SEND</div>
  </div>
</footer>
<p class="copyright abs">2017 Copyright - DesksetShiftCrew.com - Harlow Consulting, LLC<br>All product and company names are trademarks or registered trademarks of<br>their respective holders. Use of them does not imply any affiliation with or endorsement by them.</p>

</body>
</html>
```